Business Card Design

Hello,
I try and keep my business card fresh and current. So about every year i get a new one. This year I'd like something with a white background and black lettering.
Before you start - I do not want my phone number or any other description on the card other than my url and my email.

I'd like a double sided business card with
TobFarnsby.com on one side

and

Tob@TobFarnsby.com on the other side of the card

Thinking very minimalistic and modern.
I don't have a particular font i mind or how to capitalize my name or website. This card will lead people to my new website that is being designed to showcase my photography and music.

* Initial thought was the front side of the card having a grid-like pattern built out of dashes or periods, with my website sitting within the pattern and on the back side my email on a stark white background. But that might look completely lame - haha.

I'm looking forward to seeing what you come up with.

thank you,
- tob farnsby

Reason: Want to spend some more time with the designs and add a little $. thanks for all the designs - tob

Wanted to add a little $ and spend some more time with the designs.

big thanks to all who have submitted work 

- tob

Industry/Entity Type

Business

Contact Information for Business Card

www.tobfarnsby.com
tob@tobfarnsby.com

Colors
000000
ffffff

Requirements
Must have
• tobfarnsby.com
tob@tobfarnsby.com
Should not have
• phone number
any description of what i do, photography or music

```html
<!DOCTYPE html>
<html lang="en">
<head>
<meta charset="utf-8">
<title>Tob Farnsby – Business Card</title>
<link rel="stylesheet" href="https://fonts.googleapis.com/css2?family=Dancing+Script:wght@400&display=swap">
<style>
  :root {
    --backdrop: #e4e4e4;
    --card: #ffffff;
    --ink: #000000;
    --card-shadow: rgba(0, 0, 0, 0.18);
  }
  * { box-sizing: border-box; margin: 0; padding: 0; }
  html, body {
    width: 1200px;
    height: 900px;
    overflow: hidden;
    background: var(--backdrop);
  }
  .stage {
    width: 1200px;
    height: 900px;
    display: flex;
    align-items: center;
    justify-content: center;
    gap: 60px;
  }
  .card {
    width: 520px;
    height: 297px;
    background: var(--card);
    border-radius: 22px;
    box-shadow: 0 6px 18px var(--card-shadow);
    overflow: hidden;
  }
  .card svg { display: block; width: 100%; height: 100%; }
  .card-rule { stroke: var(--ink); stroke-width: 1.6; fill: none; }
  .card-text {
    font-family: "Dancing Script", cursive;
    font-size: 34px;
    fill: var(--ink);
  }
</style>
</head>
<body>
  <main class="stage">
    <section class="card card-back" aria-label="Card back: email">
      <svg viewBox="0 0 520 297" xmlns="http://www.w3.org/2000/svg">
        <line class="card-rule" x1="0" y1="162" x2="122" y2="162"/>
        <text class="card-text" x="122" y="162" textLength="276" lengthAdjust="spacingAndGlyphs">Tob@TobFarnsby.com</text>
        <line class="card-rule" x1="398" y1="146" x2="520" y2="146"/>
      </svg>
    </section>
    <section class="card card-front" aria-label="Card front: website">
      <svg viewBox="0 0 520 297" xmlns="http://www.w3.org/2000/svg">
        <line class="card-rule" x1="0" y1="162" x2="122" y2="162"/>
        <text class="card-text" x="122" y="162" textLength="276" lengthAdjust="spacingAndGlyphs">www.TobFarnsby.com</text>
        <line class="card-rule" x1="398" y1="146" x2="520" y2="146"/>
      </svg>
    </section>
  </main>
</body>
</html>
```